Founder / concept developer needs business card // Consultant needs VCARD

I need a business card for me as a founding consultant in Berlin. I advise entrepreneurs, especially in the design of business ideas, business plans or financing applications. More information about this in the annexes. My USP: I design / structure complex ideas and projects convincingly so that my client is successful. I want to communicate professionalism, effectiveness and clarity. Colors like from the range BLACK-GRAY-GREEN. I am 27 years old, I have studied business for 7 years. Attachments: - Business card design (only idea, do not focus on it) - Website screenshot (only idea, do not focus on it)

Target Market(s)

Target group: Founder (20-50 yrs, m / w, needy, in "break-up phase") and CONTRACTOR / "financier" (30-55 yrs, m / w, often public service "routine-oriented"). The foundations are in quite different industries: digital, craft, tourism, retail, services, etc. Almost all German.

Industry/Entity Type

Consultant

Contact Information for Business Card

Lukas Brenner
M. Sc., International Business Administration
Gründungsberater, Konzeptentwickler
www.falkor-plan.de
kontakt@falkor-plan.de
Tel. 0157 284 3361

Colors

Designer to choose colors to be used in the design.

Requirements
Must have
• Professionalism, persuasiveness, clarity
Nice to have
• memorability
Should not have
• Schnörkelei

```html
<!DOCTYPE html>
<html lang="de">
<head>
<meta charset="utf-8">
<title>Lukas Brenner – Visitenkarte</title>
<link href="https://fonts.googleapis.com/css2?family=Bebas+Neue&family=Lato:wght@400;700&display=swap" rel="stylesheet">
<style>
  :root {
    --stage: #e4e4e2;
    --card-dark: #1c1c1c;
    --card-light: #f7f7f7;
    --ink: #222222;
    --ink-soft: #555555;
    --grey-type: #a9a9a9;
    --grey-line: #5a5a5a;
    --band: #3a3a3a;
  }
  * { margin: 0; padding: 0; box-sizing: border-box; }
  html, body { width: 1200px; height: 800px; overflow: hidden; }
  body {
    background: var(--stage);
    display: flex;
    align-items: center;
    justify-content: center;
    gap: 40px;
    font-family: "Lato", sans-serif;
  }
  .card {
    position: relative;
    width: 540px;
    height: 350px;
    box-shadow: 0 10px 30px rgba(0,0,0,0.18);
    overflow: hidden;
  }

  /* Back side */
  .card-back { background: var(--card-dark); }
  .greeting {
    position: absolute;
    right: 44px;
    top: 26px;
    text-align: right;
    font-family: "Bebas Neue", sans-serif;
    font-size: 78px;
    line-height: 0.86;
    color: var(--grey-type);
  }
  .degree {
    position: absolute;
    right: 44px;
    top: 232px;
    text-align: right;
    font-family: "Bebas Neue", sans-serif;
    color: var(--grey-type);
    line-height: 1.1;
  }
  .degree .field { font-size: 24px; letter-spacing: 0.3px; }
  .degree .title { font-size: 22px; }
  .back-rule {
    position: absolute;
    right: 44px;
    top: 296px;
    width: 250px;
    height: 1px;
    background: var(--grey-line);
  }
  .back-web {
    position: absolute;
    right: 44px;
    top: 308px;
    font-size: 15px;
    color: var(--grey-line);
    letter-spacing: 0.3px;
  }

  /* Front side */
  .card-front { background: var(--card-light); }
  .edge-band {
    position: absolute;
    left: 0; top: 0; bottom: 0;
    width: 24px;
    background: var(--band);
  }
  .contact-list {
    position: absolute;
    left: 240px;
    top: 28px;
    list-style: none;
  }
  .contact-item {
    display: flex;
    align-items: flex-start;
    gap: 12px;
    height: 52px;
  }
  .contact-item .bar {
    width: 4px;
    height: 40px;
    background: var(--ink);
  }
  .contact-item svg { width: 14px; height: 14px; margin-top: 2px; flex: none; }
  .contact-item p {
    font-size: 12.5px;
    line-height: 1.45;
    color: var(--ink-soft);
  }
  .name {
    position: absolute;
    left: 52px;
    top: 180px;
    font-family: "Bebas Neue", sans-serif;
    font-size: 80px;
    line-height: 0.82;
    color: var(--ink);
  }
  .role-label {
    position: absolute;
    left: 280px;
    top: 294px;
    background: var(--band);
    color: #e9e9e9;
    font-size: 12px;
    letter-spacing: 1px;
    padding: 5px 12px;
  }
</style>
</head>
<body>

  <section class="card card-back" aria-label="Kartenrückseite">
    <h1 class="greeting">Hi,<br>I am<br>Lukas</h1>
    <div class="degree">
      <div class="field">International Business Administration</div>
      <div class="title">M. Sc.,</div>
    </div>
    <div class="back-rule"></div>
    <p class="back-web">www.falkor-plan.de</p>
  </section>

  <section class="card card-front" aria-label="Kartenvorderseite">
    <div class="edge-band"></div>

    <ul class="contact-list">
      <li class="contact-item">
        <span class="bar"></span>
        <svg viewBox="0 0 14 14" aria-hidden="true"><path d="M7 1a4 4 0 0 0-4 4c0 3 4 8 4 8s4-5 4-8a4 4 0 0 0-4-4zm0 5.5A1.5 1.5 0 1 1 7 3.5a1.5 1.5 0 0 1 0 3z" fill="#222"/></svg>
        <p>22, 3rd Floor,<br>Kanalhaus, Berlin 10997</p>
      </li>
      <li class="contact-item">
        <span class="bar"></span>
        <svg viewBox="0 0 14 14" aria-hidden="true"><rect x="3.5" y="1" width="7" height="12" rx="1.2" fill="none" stroke="#222" stroke-width="1.4"/><circle cx="7" cy="11" r="0.7" fill="#222"/></svg>
        <p>(office) - 0157 284 3361<br>(mobile) - 0157 284 3361</p>
      </li>
      <li class="contact-item">
        <span class="bar"></span>
        <svg viewBox="0 0 14 14" aria-hidden="true"><rect x="1" y="3" width="12" height="8" fill="#222"/><path d="M1 3l6 4.5L13 3" fill="none" stroke="#f7f7f7" stroke-width="1"/></svg>
        <p>kontakt@falkor-plan.de<br>www.falkor-plan.de</p>
      </li>
    </ul>

    <h2 class="name">Lukas<br>Brenner</h2>
    <div class="role-label">BUSINESS ADMINISTRATION</div>
  </section>

</body>
</html>
```